Business Card Design Project

I am a psychotherapist, counselor and expressive arts therapist (means I use every art form imaginable in the service of healing). I'm just starting out in private practice in San Francisco, CA. I work with individual adults, children and families. I'd like the card to mirror the simplicity and color palate of my website. I also would love if there is a symbol, image of fire, flame or spark (that is warming, not frightening).

Check out my website: www.lorabecketmft.com

I want the cards to be printed in letter press so please keep that in mind!

Target Market(s)

Upper Middle Class Adults who are progressively minded, artistic or artists, open to psychotherapy, interested in health & healing.

Industry/Entity Type

Business

Requirements
Must have
• Text to be included:

Lora Becket
Counseling, Psychotherapy & Expressive Arts

2914 Alderwood Avenue, Suite D
San Francisco, CA 94127
p. 415.206.3791
lorajanebecket@meadowpost.net

www.lorabecketmft.com

MFT License Number 48671

It's OK to abbreviate Number to # or Street to St., etc.

Must be compatible with letter press printing.
Nice to have
• I don't have a logo. I don't expect designers to necessarily create one for me, but if someone comes up with a simple image (see above about flame), that would be great. I don't have much of a budget now, but expect that to change in the next year or so and then could buy a logo for my website, future letterhead, etc.

```html
<!DOCTYPE html>
<html lang="en">
<head>
<meta charset="utf-8">
<title>Lora Becket — Business Card</title>
<link rel="stylesheet" href="https://fonts.googleapis.com/css2?family=Questrial&display=swap">
<style>
  :root {
    --backdrop: #2f323a;
    --card-stock: #e4e4e2;
    --ink: #2b2b2b;
    --ink-soft: #3a3a3a;
    --flame-red: #d8261c;
  }
  html, body {
    margin: 0;
    padding: 0;
    width: 1200px;
    height: 900px;
    overflow: hidden;
    background: var(--backdrop);
  }
  .stage {
    width: 1200px;
    height: 900px;
    display: flex;
    align-items: center;
    justify-content: center;
  }
  .business-card {
    width: 420px;
    height: 735px;
    background: var(--card-stock);
    box-sizing: border-box;
    display: flex;
    flex-direction: column;
    align-items: center;
    font-family: "Questrial", "Century Gothic", sans-serif;
    color: var(--ink);
    text-align: center;
  }
  .brand-mark {
    margin-top: 170px;
    height: 150px;
    display: flex;
    align-items: center;
    justify-content: center;
    gap: 14px;
  }
  .brand-mark__dot {
    width: 26px;
    height: 26px;
    border-radius: 50%;
    background: var(--flame-red);
  }
  .brand-mark__name {
    font-size: 30px;
    color: var(--flame-red);
  }
  .practitioner-name {
    margin: 40px 0 0;
    font-size: 34px;
    font-weight: 400;
    letter-spacing: 0.5px;
  }
  .practice-focus {
    margin: 6px 0 0;
    font-size: 18px;
    line-height: 1.3;
    color: var(--ink-soft);
  }
  .contact {
    margin: 30px 0 0;
    font-size: 19px;
    line-height: 1.4;
  }
  .address {
    margin: 26px 0 0;
    font-size: 19px;
    line-height: 1.4;
    font-style: normal;
  }
  .license {
    margin: 34px 0 0;
    font-size: 17px;
    color: var(--ink-soft);
  }
</style>
</head>
<body>
  <main class="stage">
    <article class="business-card">
      <div class="brand-mark">
        <span class="brand-mark__dot" aria-hidden="true"></span>
        <span class="brand-mark__name">Lora Becket</span>
      </div>
      <h1 class="practitioner-name">Lora Becket</h1>
      <p class="practice-focus">Counseling, Psychotherapy<br>&amp; Expressive Arts</p>
      <p class="contact">lorajanebecket@meadowpost.net<br>p. 415.206.3791</p>
      <address class="address">2914 Alderwood Avenue, Suite D<br>San Francisco, CA 94127</address>
      <p class="license">MFT License Number 48671</p>
    </article>
  </main>
</body>
</html>
```